Virtual Racing Community for Runners Needs a Refreshed Web Design

We are a STARTUP. The current website consists of 3 main pages that function well; however, they are not producing the proper conversions because we need a more professional look and better execution of our great ideas.

First page: landing page that needs to be intriguing, sleek, create urgency, incorporate our call to action and most importantly get the consumer to click a button to get to second page. www.lopendash.com

Second page: sign up page that incorporates our already existing postwren form that doesn't take the viewer away from the page on incorrect form field entry. On successful completion needs to inform the viewer to check the email and confirm (possibly in spam) and open third page. http://www.lopendash.com/beta.html

Third page: preorder page that allows the user prepurchase through a well working form through "www.getmarlowpay.com." This interface works really well; however, the graphics and page need to really entice the viewer to buy. http://www.lopendash.com/preorder.html

And that's it!!! Simple 3 pages that function currently 95% how we want it, but really needs that creative touch to push it to the next level!

Contact us with any other questions!

Reason: I have provided numerous feedback and am awaiting redesigns. Have it narrowed down to 2 designers. Need time to vet with stakeholders.

```html
<!DOCTYPE html>
<html lang="en">
<head>
<meta charset="utf-8">
<title>lopendash — Race On Your Own Terms</title>
<link rel="stylesheet" href="https://fonts.googleapis.com/css2?family=Oswald:wght@300;400;500&family=Roboto:wght@500;700;900&display=swap">
<style>
  :root {
    --ink-dark: #1a0d08;
    --ink-grey: #4a4544;
    --accent-red: #e8413f;
    --cream: #fff8ec;
    --white: #ffffff;
    --gold: #b89a5e;
    --ring-orange: #f08a1c;
    --disc-brown: #3a1a0c;
    --button-fill: #1c0f0a;
  }
  * { margin: 0; padding: 0; box-sizing: border-box; }
  html, body { width: 1200px; height: 723px; overflow: hidden; }
  body { position: relative; background: #2a140a; font-family: "Roboto", Arial, sans-serif; }

  .hero-photo {
    position: absolute; inset: 0;
    background:
      radial-gradient(ellipse 55% 45% at 72% 38%, rgba(255,236,150,0.95) 0%, rgba(250,190,60,0.7) 35%, rgba(0,0,0,0) 75%),
      radial-gradient(ellipse 70% 60% at 55% 80%, rgba(220,60,20,0.85) 0%, rgba(150,40,15,0.6) 50%, rgba(0,0,0,0) 85%),
      linear-gradient(180deg, #6b4a1e 0%, #d9902a 38%, #e46a1c 62%, #8e2a10 100%);
  }
  .hero-photo::after {
    content: ""; position: absolute; inset: 0;
    background: radial-gradient(ellipse 75% 70% at 55% 45%, rgba(0,0,0,0) 55%, rgba(25,12,5,0.7) 100%);
  }

  .brand-badge {
    position: absolute; left: 508px; top: -84px; width: 184px; height: 184px;
  }
  .brand-name {
    position: absolute; left: 0; top: 12px; width: 1200px; text-align: center;
    font-family: "Oswald", Arial, sans-serif; font-weight: 400; font-size: 22px;
    color: var(--ink-grey); letter-spacing: 0.5px;
  }

  .headline {
    position: absolute; left: 0; top: 148px; width: 1200px; text-align: center;
    font-family: "Oswald", Arial, sans-serif; font-weight: 300; font-size: 66px;
    line-height: 1; letter-spacing: -0.5px;
  }
  .headline .w-race { color: var(--accent-red); }
  .headline .w-on { color: var(--white); }
  .headline .w-your { color: var(--ink-grey); }
  .headline .w-own { color: var(--cream); }
  .headline .w-terms { color: var(--ink-dark); }

  .tagline {
    position: absolute; left: 0; top: 216px; width: 1200px; text-align: center;
    font-family: "Oswald", Arial, sans-serif; font-weight: 500; font-size: 33px;
    line-height: 1.1; color: var(--white); letter-spacing: -0.3px;
  }

  .countdown { position: absolute; top: 330px; left: 0; width: 1200px; height: 130px; }
  .timer { position: absolute; top: 0; width: 130px; height: 130px; }
  .timer svg { position: absolute; inset: 0; }
  .timer-value {
    position: absolute; left: 0; top: 22px; width: 130px; text-align: center;
    font-family: "Roboto", Arial, sans-serif; font-weight: 700; font-size: 68px;
    line-height: 1; color: var(--white); letter-spacing: -2px;
  }
  .timer-unit {
    position: absolute; left: 0; top: 96px; width: 130px; text-align: center;
    font-weight: 700; font-size: 14px; color: var(--white);
  }
  .timer-hours { left: 293px; }
  .timer-minutes { left: 535px; }
  .timer-seconds { left: 776px; }

  .cta-button {
    position: absolute; left: 446px; top: 574px; width: 309px; height: 55px;
    border: 4px solid var(--white); border-radius: 4px; background: var(--button-fill);
    color: var(--white); font-weight: 700; font-size: 14.5px; text-align: center;
    line-height: 47px; text-decoration: none; letter-spacing: 0.1px;
  }
  .cta-note {
    position: absolute; left: 0; top: 635px; width: 1200px; text-align: center;
    font-weight: 500; font-size: 11.5px; color: var(--white);
  }
</style>
</head>
<body>
  <div class="hero-photo" role="img" aria-label="Photo of a runner's legs and red running shoes on an asphalt road in warm golden sunrise light"></div>

  <svg class="brand-badge" viewBox="0 0 184 184" aria-hidden="true">
    <circle cx="92" cy="92" r="88" fill="none" stroke="var(--gold)" stroke-width="4"/>
    <circle cx="92" cy="92" r="82" fill="var(--white)"/>
  </svg>
  <div class="brand-name">lopendash</div>

  <h1 class="headline">
    <span class="w-race">RACE</span> <span class="w-on">ON</span> <span class="w-your">YOUR</span> <span class="w-own">OWN</span> <span class="w-terms">TERMS</span>
  </h1>
  <p class="tagline">WHEREVER. WHATEVER. WHENEVER.</p>

  <div class="countdown">
    <div class="timer timer-hours">
      <svg viewBox="0 0 130 130" aria-hidden="true">
        <circle cx="65" cy="65" r="62" fill="none" stroke="var(--white)" stroke-width="3" stroke-dasharray="93.4 4" stroke-dashoffset="2"/>
        <circle cx="65" cy="65" r="58" fill="none" stroke="var(--ring-orange)" stroke-width="4"/>
        <circle cx="65" cy="65" r="54" fill="var(--disc-brown)" fill-opacity="0.88" stroke="var(--white)" stroke-width="1.5"/>
      </svg>
      <div class="timer-value">24</div>
      <div class="timer-unit">HR</div>
    </div>
    <div class="timer timer-minutes">
      <svg viewBox="0 0 130 130" aria-hidden="true">
        <circle cx="65" cy="65" r="62" fill="none" stroke="var(--white)" stroke-width="3" stroke-dasharray="93.4 4" stroke-dashoffset="2"/>
        <circle cx="65" cy="65" r="58" fill="none" stroke="var(--ring-orange)" stroke-width="4"/>
        <circle cx="65" cy="65" r="54" fill="var(--disc-brown)" fill-opacity="0.88" stroke="var(--white)" stroke-width="1.5"/>
      </svg>
      <div class="timer-value">60</div>
      <div class="timer-unit">MIN</div>
    </div>
    <div class="timer timer-seconds">
      <svg viewBox="0 0 130 130" aria-hidden="true">
        <circle cx="65" cy="65" r="62" fill="none" stroke="var(--white)" stroke-width="3" stroke-dasharray="93.4 4" stroke-dashoffset="2"/>
        <circle cx="65" cy="65" r="58" fill="none" stroke="var(--ring-orange)" stroke-width="4"/>
        <circle cx="65" cy="65" r="54" fill="var(--disc-brown)" fill-opacity="0.88" stroke="var(--white)" stroke-width="1.5"/>
      </svg>
      <div class="timer-value">60</div>
      <div class="timer-unit">SEC</div>
    </div>
  </div>

  <a class="cta-button" href="http://www.lopendash.com/beta.html">SIGNUP BEFORE TIME RUNS OUT</a>
  <p class="cta-note">For a Limited Time be the First to Receive Early Access</p>
</body>
</html>
```